Eye catching Bottle label for pink gin targeting women 25+

We need a new label for a re-launch of our shimmering strawberry pink gin liqueur. We would like it to look premium and eye catching on the shelf. We have 2 labels we require, one for 200ml bottle (2x2 inches) and one for 500ml bottle 4x4 inches). Label must state the ml of the bottle abd that it is 18.75%Vol. Also say Shimmering Strawberry Gin Liqueur with the brand name at the top - Marlow Tide. We have a logo but it doesn't need to be used if it doesn't work with the design/colours. The gin is presented in a clear bottle and is pink and sparkly. See uploaded image for reference.

Target Market(s)

Women aged 25-45

Font styles to use
Decorative

Colors
f59296
fbd4d5
eea4c8

Requirements
Must have
• Bottle size - 500ml/200ml
• Must say 18.75% Vol
• Must have brand name - Marlow Tide
• Must have product name - Shimmering Pink Strawberry
• Must say - Gin Liqueur
Nice to have
• Some sort of floral or swirley background detail would be nice
Should not have
• Must not appeal to children

```html
<!DOCTYPE html>
<html lang="en">
<head>
<meta charset="utf-8">
<title>Marlow Tide – Shimmering Pink Strawberry Gin Liqueur Label</title>
<link rel="stylesheet" href="https://fonts.googleapis.com/css2?family=Saira+Condensed:wght@500;700&display=swap">
<style>
  :root {
    --backdrop: #e2e2e2;
    --label-paper: #f4f4f4;
    --berry-pink: #e0429a;
    --berry-soft: #eea4c8;
    --diamond-start: #e65aa8;
    --diamond-end: #b23fd0;
    --teal: #3e7f80;
    --ink: #2f2f2f;
    --brand-grey: #4a4a4a;
  }
  html, body {
    margin: 0;
    padding: 0;
    width: 1200px;
    height: 900px;
    overflow: hidden;
    background: var(--backdrop);
  }
  .canvas {
    position: relative;
    width: 1200px;
    height: 900px;
    display: flex;
    align-items: center;
    justify-content: center;
  }
  .label {
    position: relative;
    width: 600px;
    height: 780px;
    background: var(--label-paper);
    overflow: hidden;
    font-family: "Saira Condensed", sans-serif;
  }
  .label__diamond {
    position: absolute;
    inset: 0;
    width: 100%;
    height: 100%;
  }
  .strawberry {
    position: absolute;
    width: 110px;
    height: 140px;
    border-radius: 50% 50% 48% 48% / 40% 40% 60% 60%;
    background: radial-gradient(circle at 45% 40%, #f7d3e6, var(--berry-soft));
    opacity: 0.75;
  }
  .strawberry--top-left { left: -30px; top: 110px; }
  .strawberry--top-right { right: -22px; top: 150px; }
  .strawberry--bottom-left { left: -62px; top: 580px; }
  .strawberry--bottom-right { right: -64px; top: 620px; }
  .brand {
    position: absolute;
    top: 120px;
    left: 0;
    right: 0;
    display: flex;
    align-items: center;
    justify-content: center;
    gap: 14px;
    font-weight: 500;
    font-size: 64px;
    letter-spacing: 2px;
    color: var(--brand-grey);
  }
  .brand__mark {
    width: 16px;
    height: 16px;
    border-radius: 50%;
    background: var(--brand-grey);
  }
  .product-name {
    position: absolute;
    top: 338px;
    left: 0;
    right: 0;
    text-align: center;
    font-weight: 700;
    font-size: 40px;
    letter-spacing: 1px;
    color: var(--berry-pink);
  }
  .product-type {
    position: absolute;
    top: 378px;
    left: 0;
    right: 0;
    text-align: center;
    font-weight: 700;
    font-size: 128px;
    line-height: 1.1;
    letter-spacing: 3px;
    color: var(--teal);
  }
  .abv {
    position: absolute;
    top: 683px;
    left: 0;
    right: 0;
    text-align: center;
    font-weight: 500;
    font-size: 26px;
    color: var(--ink);
  }
  .volume {
    position: absolute;
    top: 716px;
    left: 0;
    right: 0;
    text-align: center;
    font-weight: 500;
    font-size: 26px;
    color: var(--berry-pink);
  }
</style>
</head>
<body>
<main class="canvas">
  <section class="label">
    <svg class="label__diamond" viewBox="0 0 600 780" aria-hidden="true">
      <defs>
        <linearGradient id="diamondStroke" x1="0" y1="0" x2="1" y2="1">
          <stop offset="0" stop-color="var(--diamond-start)"/>
          <stop offset="1" stop-color="var(--diamond-end)"/>
        </linearGradient>
      </defs>
      <polygon points="300,135 600,420 300,705 0,420" fill="none" stroke="url(#diamondStroke)" stroke-width="5"/>
      <polygon points="300,148 586,420 300,692 14,420" fill="none" stroke="url(#diamondStroke)" stroke-width="1.5" opacity="0.6"/>
    </svg>

    <div class="strawberry strawberry--top-left" role="img" aria-label="Line illustration of a strawberry"></div>
    <div class="strawberry strawberry--top-right" role="img" aria-label="Line illustration of a strawberry"></div>
    <div class="strawberry strawberry--bottom-left" role="img" aria-label="Line illustration of a strawberry"></div>
    <div class="strawberry strawberry--bottom-right" role="img" aria-label="Line illustration of a strawberry"></div>

    <div class="brand"><span class="brand__mark"></span><span class="brand__name">Marlow Tide</span></div>

    <p class="product-name" style="margin:0">SHIMMERING PINK STRAWBERRY</p>
    <h1 class="product-type" style="margin:0">GIN LIQUER</h1>

    <p class="abv" style="margin:0">18.75% VOL</p>
    <p class="volume" style="margin:0">500ML</p>
  </section>
</main>
</body>
</html>
```